Studying Effectively To Do List

I am looking to design a new "Study To Do List" for High School students (Ages 15 - 18) . This will be printed as an A4 notepad and so should only be a single A4 page.

The Design will need to be professional and look semi-serious but also be appealing to High school students (Ages 15 - 18) and should NOT be gender specific.

I have attached a word document outlining the structure of the page. The space provided should be large enough that people can write in it comfortably.

The notepad will most likely be printed in black and white but I'm also looking at coloured options - colours should be kept to a minimum.

This will be printed professionally and should also include a 3mm bleed.

The design should also include the business logo (included in the word document)

Target Market(s)

High School students (Ages 15 - 18). Both genders

Industry/Entity Type

Education

Font styles to use
Serif
Sans Serif

Requirements
Must have
• Please see the word document attached.
Should not have
• Too much colour

```html
<!DOCTYPE html>
<html lang="en">
<head>
<meta charset="utf-8">
<title>Study To Do List</title>
<link href="https://fonts.googleapis.com/css2?family=Montserrat:wght@600;700&family=Open+Sans:wght@300;400&display=swap" rel="stylesheet">
<style>
  :root{
    --ink:#1f1f1f;
    --rule:#3a3a3a;
    --line:#b9b9b9;
    --box-fill:#dcdcdc;
    --box-edge:#8a8a8a;
    --paper:#ffffff;
    --accent:#f28c1e;
    --brand:#1d3b57;
  }
  *{margin:0;padding:0;box-sizing:border-box}
  html,body{width:848px;height:1200px;overflow:hidden;background:var(--paper)}
  .page{position:relative;width:848px;height:1200px;font-family:"Open Sans",Arial,sans-serif;color:var(--ink)}
  .backdrop{position:absolute;inset:0;background:radial-gradient(circle at 50% 50%,#fafafa,#f2f2f2)}
  .date{position:absolute;left:545px;top:60px;display:flex;align-items:flex-end;width:247px;font-family:"Montserrat",sans-serif;font-weight:600;font-size:13px;letter-spacing:.5px}
  .date svg{margin-right:4px}
  .date .fill{flex:1;border-bottom:1px solid var(--line);margin-left:6px;height:14px}
  .section{position:absolute;display:flex;align-items:flex-end;border-bottom:1px solid var(--rule);height:24px}
  .section .tab{width:24px;height:23px;background:var(--box-fill);border-left:2px solid var(--box-edge);margin-right:6px;align-self:flex-end}
  .section h2{font-family:"Montserrat",sans-serif;font-weight:600;font-size:18px;line-height:22px;letter-spacing:.3px}
  .section.small h2{font-size:15px}
  .numrow{position:absolute;display:flex;align-items:flex-end;height:20px}
  .num{width:18px;height:19px;border:1px solid var(--box-edge);background:var(--paper);font-size:14px;line-height:17px;text-align:center;margin-right:4px}
  .numrow .fill{flex:1;border-bottom:1px solid var(--line);height:1px}
  .rows{position:absolute;left:81px;width:711px}
  .row{display:flex;align-items:flex-end;height:28.5px;font-weight:300;font-size:16px;padding-bottom:5px}
  .row span{line-height:18px;white-space:nowrap}
  .row .fill{flex:1;border-bottom:1px solid var(--line);margin-left:5px;height:1px}
  .row .fill.short{flex:0 0 233px}
  .row .due{margin-left:30px}
  .practice{position:absolute;left:479px;width:313px}
  .practice .fill{height:28.5px;border-bottom:1px solid var(--line)}
  .practice .fill.cut{width:250px}
  .brand{position:absolute;left:736px;top:1082px;display:flex;align-items:center;gap:5px}
  .brand .dot{width:30px;height:30px;border-radius:50%;background:var(--accent)}
  .brand span{font-family:"Montserrat",sans-serif;font-weight:700;font-size:16px;color:var(--brand)}
</style>
</head>
<body>
<div class="page">
  <div class="backdrop" role="img" aria-label="Faint hand-drawn school doodle pattern background"></div>

  <div class="date">
    <svg width="20" height="18" viewBox="0 0 20 18"><rect x="1" y="3" width="18" height="14" fill="none" stroke="#1f1f1f" stroke-width="2"/><rect x="1" y="3" width="18" height="4" fill="#1f1f1f"/><rect x="5" y="0" width="2" height="4" fill="#1f1f1f"/><rect x="13" y="0" width="2" height="4" fill="#1f1f1f"/><g fill="#1f1f1f"><rect x="4" y="9" width="3" height="2"/><rect x="9" y="9" width="3" height="2"/><rect x="14" y="9" width="3" height="2"/><rect x="4" y="13" width="3" height="2"/><rect x="9" y="13" width="3" height="2"/><rect x="14" y="13" width="3" height="2"/></g></svg>
    DATE:<div class="fill"></div>
  </div>

  <div class="section" style="left:51px;top:86px;width:741px"><div class="tab"></div><h2>REVISION</h2></div>
  <div class="numrow" style="left:77px;top:120px;width:337px"><div class="num">1</div><div class="fill"></div></div>
  <div class="numrow" style="left:77px;top:148px;width:337px"><div class="num">2</div><div class="fill"></div></div>
  <div class="numrow" style="left:77px;top:177px;width:337px"><div class="num">3</div><div class="fill"></div></div>
  <div class="numrow" style="left:77px;top:205px;width:337px"><div class="num">4</div><div class="fill"></div></div>
  <div class="numrow" style="left:440px;top:120px;width:352px"><div class="num">5</div><div class="fill"></div></div>
  <div class="numrow" style="left:440px;top:148px;width:352px"><div class="num">6</div><div class="fill"></div></div>
  <div class="numrow" style="left:440px;top:177px;width:352px"><div class="num">7</div><div class="fill"></div></div>
  <div class="numrow" style="left:440px;top:205px;width:352px"><div class="num">8</div><div class="fill"></div></div>

  <div class="section" style="left:51px;top:237px;width:741px"><div class="tab"></div><h2>HOMEWORK</h2></div>
  <div class="rows" style="top:266px">
    <div class="row"><span>Subject:</span><div class="fill"></div></div>
    <div class="row"><span>Task:</span><div class="fill"></div></div>
    <div class="row"><span>Subject:</span><div class="fill"></div></div>
    <div class="row"><span>Task:</span><div class="fill"></div></div>
    <div class="row"><span>Subject:</span><div class="fill"></div></div>
    <div class="row"><span>Task:</span><div class="fill"></div></div>
    <div class="row"><span>Subject:</span><div class="fill"></div></div>
    <div class="row"><span>Task:</span><div class="fill"></div></div>
    <div class="row"><span>Subject:</span><div class="fill"></div></div>
    <div class="row"><span>Task:</span><div class="fill"></div></div>
    <div class="row"><span>Subject:</span><div class="fill"></div></div>
    <div class="row"><span>Task:</span><div class="fill"></div></div>
  </div>

  <div class="section" style="left:51px;top:615px;width:741px"><div class="tab"></div><h2>ASSESSMENTS</h2></div>
  <div class="rows" style="top:644px">
    <div class="row"><span>Assessment:</span><div class="fill short"></div><span class="due">Due</span><div class="fill"></div></div>
    <div class="row"><span>Element:</span><div class="fill"></div></div>
    <div class="row"><span>Assessment:</span><div class="fill short"></div><span class="due">Due</span><div class="fill"></div></div>
    <div class="row"><span>Element:</span><div class="fill"></div></div>
    <div class="row"><span>Assessment:</span><div class="fill short"></div><span class="due">Due</span><div class="fill"></div></div>
    <div class="row"><span>Element:</span><div class="fill"></div></div>
    <div class="row"><span>Assessment:</span><div class="fill short"></div><span class="due">Due</span><div class="fill"></div></div>
    <div class="row"><span>Element:</span><div class="fill"></div></div>
    <div class="row"><span>Assessment:</span><div class="fill short"></div><span class="due">Due</span><div class="fill"></div></div>
    <div class="row"><span>Element:</span><div class="fill"></div></div>
    <div class="row"><span>Assessment:</span><div class="fill short"></div><span class="due">Due</span><div class="fill"></div></div>
    <div class="row"><span>Element:</span><div class="fill"></div></div>
  </div>

  <div class="section small" style="left:53px;top:993px;width:363px"><div class="tab"></div><h2>NOTES</h2></div>
  <div class="section small" style="left:444px;top:993px;width:348px"><div class="tab" style="margin-right:10px"></div><h2>PRACTICE</h2></div>

  <div class="numrow" style="left:77px;top:1027px;width:161px"><div class="num">1</div><div class="fill"></div></div>
  <div class="numrow" style="left:77px;top:1056px;width:161px"><div class="num">2</div><div class="fill"></div></div>
  <div class="numrow" style="left:77px;top:1084px;width:161px"><div class="num">3</div><div class="fill"></div></div>
  <div class="numrow" style="left:77px;top:1113px;width:161px"><div class="num">4</div><div class="fill"></div></div>
  <div class="numrow" style="left:254px;top:1027px;width:162px"><div class="num">5</div><div class="fill"></div></div>
  <div class="numrow" style="left:254px;top:1056px;width:162px"><div class="num">6</div><div class="fill"></div></div>
  <div class="numrow" style="left:254px;top:1084px;width:162px"><div class="num">7</div><div class="fill"></div></div>
  <div class="numrow" style="left:254px;top:1113px;width:162px"><div class="num">8</div><div class="fill"></div></div>

  <div class="practice" style="top:1017px">
    <div class="fill"></div>
    <div class="fill"></div>
    <div class="fill cut"></div>
    <div class="fill cut"></div>
  </div>

  <div class="brand"><div class="dot"></div><span>Studora</span></div>
</div>
</body>
</html>
```